Business Card Design Project

New Private residential substance abuse treatment facility in Mapleton, UT. Facility located in elegant 11,000 home with stunning views of the mountains. Wish to incorporate colored logo. Business name- Cedar Brook Wellness. Facility is Tudor style with traditional furnishings, an overhead picture is attached. Lettering in a simple scroll or old english style. Must be easy to read with clear moderetly large font.
Updates

It seems the project time frame listed was not correct- it is a week.

Target Market(s)

Adults 18 and over with substance abuse issues requiring residential rehabilitation. Referral base are medical/mental health professionals, families and community agencies.

Industry/Entity Type

Residential

Colors
9bcb3b
fece3e
fbee3f

Requirements
Must have
• Clear and easy to read, professional and upscale presentation. Need logo, name, title, address, phone, fax and web page address. May add slogan later. Use same font as logo.
Nice to have
• Logo has a green mountain and a gold maple leaf so a nature themed element may work. Want to promote peaceful grounded image. Logo attached.
Should not have
• No tiny or complicated font. No modern or tech looking images. No light colored fonts.

```html
<!DOCTYPE html>
<html lang="en">
<head>
<meta charset="utf-8">
<title>Cedar Brook Wellness – Business Card</title>
<link href="https://fonts.googleapis.com/css2?family=Pinyon+Script&family=Cormorant+SC:wght@500&family=Open+Sans:wght@400&display=swap" rel="stylesheet">
<style>
  :root {
    --page-bg: #e9e5dc;
    --card-bg: #ffffff;
    --forest: #3f7f2f;
    --leaf-green: #6aa83a;
    --gold: #e2c12a;
    --sun: #fbee3f;
    --ink: #2b2b2b;
    --ink-soft: #555555;
  }
  * { box-sizing: border-box; margin: 0; padding: 0; }
  html, body { width: 1200px; height: 1023px; overflow: hidden; }
  body {
    background: var(--page-bg);
    display: flex; align-items: center; justify-content: center;
  }
  .business-card {
    position: relative;
    width: 1050px; height: 600px;
    background: var(--card-bg);
    box-shadow: 0 10px 30px rgba(0,0,0,.18);
    overflow: hidden;
  }
  .scenery {
    position: absolute; right: 0; top: 0;
    width: 420px; height: 540px;
  }
  .brand {
    position: absolute; left: 70px; top: 60px;
    display: flex; align-items: center; gap: 22px;
  }
  .brand-dot {
    width: 64px; height: 64px; border-radius: 50%;
    background: var(--leaf-green);
  }
  .brand-name {
    font-family: "Pinyon Script", cursive;
    font-size: 72px; line-height: 1; color: var(--ink);
  }
  .person { position: absolute; left: 160px; top: 200px; }
  .person-name {
    font-family: "Pinyon Script", cursive;
    font-size: 52px; color: var(--ink); line-height: 1.1;
  }
  .person-title {
    font-family: "Cormorant SC", serif;
    font-size: 22px; letter-spacing: 2px; color: var(--ink-soft);
    margin-top: 6px;
  }
  .contact-list {
    position: absolute; left: 70px; top: 340px;
    list-style: none;
    font-family: "Open Sans", sans-serif; font-size: 22px; color: var(--ink-soft);
  }
  .contact-list li { display: flex; align-items: center; gap: 14px; height: 34px; }
  .contact-icon { width: 22px; height: 22px; flex: none; }
  .address-band {
    position: absolute; left: 0; bottom: 0;
    width: 100%; height: 60px;
    background: var(--forest);
    display: flex; align-items: center; padding-left: 70px;
    font-family: "Open Sans", sans-serif; font-size: 22px; color: #fff;
  }
</style>
</head>
<body>
  <article class="business-card">
    <svg class="scenery" viewBox="0 0 420 540" role="img" aria-label="Illustration of green mountains with pine trees and large golden maple leaves">
      <defs>
        <linearGradient id="scenery-fill" x1="0" y1="0" x2="0" y2="1">
          <stop offset="0" stop-color="#f2d43a"/>
          <stop offset="0.45" stop-color="#c9c33a"/>
          <stop offset="1" stop-color="#4f8f32"/>
        </linearGradient>
      </defs>
      <path d="M420 0 H150 C190 90 200 170 120 260 C70 320 30 420 0 540 H420 Z" fill="url(#scenery-fill)"/>
    </svg>

    <div class="brand">
      <span class="brand-dot"></span>
      <span class="brand-name">Cedar Brook Wellness</span>
    </div>

    <div class="person">
      <p class="person-name">Laura J Bennett, MA</p>
      <p class="person-title">Director of Business Development</p>
    </div>

    <ul class="contact-list">
      <li>
        <svg class="contact-icon" viewBox="0 0 22 22"><rect width="22" height="22" rx="3" fill="#6aa83a"/><path d="M7 5c-1 1-1 3 1 6s4 5 6 5c1 0 2-1 2-2l-2-2-2 1c-1-1-2-2-3-3l1-2-2-2z" fill="#fff"/></svg>
        (555) 214-3087
      </li>
      <li>
        <svg class="contact-icon" viewBox="0 0 22 22"><rect width="22" height="22" rx="3" fill="#6aa83a"/><rect x="5" y="9" width="12" height="8" fill="#fff"/><rect x="7" y="4" width="8" height="5" fill="#fff"/></svg>
        (555) 214-3090
      </li>
      <li>
        <svg class="contact-icon" viewBox="0 0 22 22"><rect width="22" height="22" rx="3" fill="#6aa83a"/><rect x="7" y="4" width="8" height="14" rx="1.5" fill="#fff"/><rect x="8.5" y="6" width="5" height="8" fill="#6aa83a"/></svg>
        (555) 312-6645
      </li>
      <li>
        <svg class="contact-icon" viewBox="0 0 22 22"><rect width="22" height="22" rx="3" fill="#6aa83a"/><rect x="4" y="6" width="14" height="10" fill="#fff"/><path d="M4 6l7 6 7-6" fill="none" stroke="#6aa83a" stroke-width="1.5"/></svg>
        lbennett@cedarbrookwellness.com
      </li>
    </ul>

    <footer class="address-band">418 North Ridge Road, Pine Hollow, Utah 84000</footer>
  </article>
</body>
</html>
```